Hollowmere Farm Promotional Leaflet

The team at Hollowmere Farm can help with every aspect of managing and enhancing your home from housekeeping and professional cleaning, laundry and ironing to providing chic and contemporary flower arrangements and even food for your pets!We take pride in providing high-end, consistent and reliable professional services bespoke to you. Whether you are a busy professional working long hours, a stay-at home parent or retired; having professional help in the home gives you time to spend on the things you enjoy.We are providing a very upmarket, highly professional service and need an A5 promotional leaflet to be designed. Please refer to www.hollowmerefarm-example.co.uk and see the section on 'Home Management'The leaflet should incorporate the Hollowmere Farm logo without the 'tipi', and any suitable photography images used on the home page of the website or the 'home management' section.

Target Market(s)

high-end, affluent owners of luxury homes

Industry/Entity Type

Farm

Contact Information for Business Card

The business card design needs to be suitable for use across all of Hollowmere Farm businesses, specifically:
Hollowmere Farm Home Management - otherwise known as Hollowmere Farm @ Home (this uses the typographical logo
Hollowmere Farm Weddings & Events - this uses the 'tipi' logo

Requirements
Must have
• Design in keeping with the look and feel of the logo and website design
• www.hollowmerefarm-example.co.uk

```html
<!DOCTYPE html>
<html lang="en">
<head>
<meta charset="utf-8">
<title>Hollowmere Farm – Home Management &amp; Cleaning Services</title>
<link href="https://fonts.googleapis.com/css2?family=Raleway:wght@400;500&display=swap" rel="stylesheet">
<style>
  :root {
    --pink: #e0218a;
    --pink-soft: #f06db3;
    --lime: #a6c939;
    --ink: #4a5368;
    --paper: #ffffff;
    --room-light: #e9e4dc;
    --room-mid: #b9ad9c;
    --room-dark: #6f6658;
  }
  * { box-sizing: border-box; margin: 0; padding: 0; }
  html, body { width: 847px; height: 1200px; overflow: hidden; background: var(--paper); }
  .leaflet {
    position: relative;
    width: 847px;
    height: 1200px;
    overflow: hidden;
    background: var(--paper);
    font-family: "Raleway", Arial, sans-serif;
    color: var(--ink);
  }
  .hero-photo {
    position: absolute;
    left: 0; top: 0;
    width: 847px; height: 560px;
    background: linear-gradient(160deg, var(--room-light) 0%, #d8d0c3 45%, var(--room-mid) 75%, var(--room-dark) 100%);
  }
  .swoosh {
    position: absolute;
    left: 0; top: 380px;
    width: 847px; height: 220px;
  }
  .housekeeper-photo {
    position: absolute;
    left: 460px; top: 480px;
    width: 350px; height: 420px;
    border-radius: 150px 150px 0 0;
    background: linear-gradient(180deg, #e9dcc8 0%, #d8c6b0 35%, #3c3a44 65%, #2f2d36 100%);
  }
  .photo-base {
    position: absolute;
    left: 450px; top: 900px;
    width: 370px; height: 8px;
    background: var(--lime);
  }
  .get-in-touch {
    position: absolute;
    left: 680px; top: 790px;
    width: 112px; height: 112px;
    border-radius: 50%;
    background: var(--pink);
    color: var(--paper);
    display: flex;
    align-items: center;
    justify-content: center;
    text-align: center;
    font-weight: 500;
    font-size: 19px;
    line-height: 22px;
    transform: rotate(-12deg);
  }
  .content {
    position: absolute;
    left: 62px; top: 660px;
    width: 380px;
  }
  .headline {
    color: var(--pink);
    font-weight: 400;
    font-size: 26px;
    line-height: 30px;
    letter-spacing: 0.3px;
    text-transform: uppercase;
    margin-bottom: 22px;
  }
  .body-copy {
    font-size: 18px;
    line-height: 21.5px;
    margin-bottom: 18px;
  }
  .brand {
    position: absolute;
    left: 470px; top: 945px;
    width: 350px;
    display: flex;
    align-items: center;
    gap: 14px;
  }
  .brand-dot {
    width: 16px; height: 16px;
    border-radius: 50%;
    background: var(--pink);
    flex: none;
  }
  .brand-name {
    color: var(--pink);
    font-size: 36px;
    font-weight: 400;
    white-space: nowrap;
  }
  .contact {
    position: absolute;
    left: 470px;
    display: flex;
    align-items: center;
    gap: 12px;
    color: var(--ink);
    white-space: nowrap;
  }
  .contact-phone { top: 1055px; font-size: 25px; }
  .contact-web { top: 1110px; font-size: 18px; }
  .contact-icon { width: 26px; height: 26px; flex: none; }
</style>
</head>
<body>
<main class="leaflet">
  <div class="hero-photo" role="img" aria-label="Photograph of a bright, elegant living room with tall bookshelves, a mustard armchair and a small dog on the rug"></div>

  <svg class="swoosh" viewBox="0 0 847 220" aria-hidden="true">
    <path d="M0 70 C 250 130, 560 110, 847 30 L847 70 C 560 150, 250 170, 0 110 Z" fill="var(--lime)"/>
    <path d="M0 110 C 250 170, 560 150, 847 70 L847 100 C 560 185, 250 195, 0 135 Z" fill="var(--pink-soft)"/>
    <path d="M0 135 C 250 195, 560 185, 847 100 L847 220 L0 220 Z" fill="var(--paper)"/>
  </svg>

  <div class="housekeeper-photo" role="img" aria-label="Photograph of a smiling housekeeper in uniform holding a basket of cleaning products"></div>
  <div class="photo-base"></div>

  <div class="get-in-touch">Get in<br>touch!</div>

  <section class="content">
    <h1 class="headline">Home Management<br>&amp; Cleaning Services</h1>
    <p class="body-copy">The team at Hollowmere Farm can help with every aspect of managing and enhancing your home – from housekeeping and professional cleaning, laundry and ironing to providing chic and contemporary flower arrangements and even food for your pets!</p>
    <p class="body-copy">We take pride in providing high-end, consistent and reliable professional services bespoke to you. Whether you are a busy professional working long hours, a stay-at home parent or retired; having professional help in the home gives you time to spend on the things you enjoy.</p>
  </section>

  <div class="brand">
    <span class="brand-dot"></span>
    <span class="brand-name">Hollowmere Farm</span>
  </div>

  <div class="contact contact-phone">
    <svg class="contact-icon" viewBox="0 0 24 24" aria-hidden="true">
      <path d="M6.6 10.8a15.1 15.1 0 0 0 6.6 6.6l2.2-2.2a1 1 0 0 1 1-.25 11.4 11.4 0 0 0 3.6.57 1 1 0 0 1 1 1V20a1 1 0 0 1-1 1A17 17 0 0 1 3 4a1 1 0 0 1 1-1h3.5a1 1 0 0 1 1 1c0 1.25.2 2.45.57 3.57a1 1 0 0 1-.25 1z" fill="var(--pink)"/>
    </svg>
    <span>07700 900481</span>
  </div>

  <div class="contact contact-web">
    <svg class="contact-icon" viewBox="0 0 24 24" aria-hidden="true">
      <circle cx="12" cy="12" r="11" fill="var(--pink)"/>
      <circle cx="12" cy="12" r="6" fill="none" stroke="var(--paper)" stroke-width="1.6"/>
      <path d="M6 12h12M12 6c-2.5 3.5-2.5 8.5 0 12M12 6c2.5 3.5 2.5 8.5 0 12" fill="none" stroke="var(--paper)" stroke-width="1.3"/>
    </svg>
    <span>www.hollowmerefarm-example.co.uk</span>
  </div>
</main>
</body>
</html>
```